Business Card Design

I need a business card design for my law office based in Pasadena, California. I am a sole practitioner and I specialize in business transaction and litigation, probate and estate planning, taxation law, corporate and business formation, immigration and real estate. I want something that is simple, yet stands out.

A friend helped to create a logo about 6 years ago. I am open to new ideas to changing the logo.

Industry/Entity Type

Business

Contact Information for Business Card

Law Offices of Doran M. Vaske
482 W. Harlow Ave., Suite 312
Pasadena, CA 91108
Tel: 626-503-7719
Fax: 626-581-9046
Email: dvaske@dmvlegalgrp.example

Attorney: Doran M. Vaske

```html
<!DOCTYPE html>
<html lang="en">
<head>
<meta charset="utf-8">
<title>Law Offices of Doran M. Vaske — Business Card</title>
<link rel="stylesheet" href="https://fonts.googleapis.com/css2?family=Cinzel:wght@400;600&family=Arimo:wght@400&display=swap">
<style>
  :root {
    --canvas: #e9e7e3;
    --paper: #ffffff;
    --ink: #1a1a1a;
    --ink-soft: #3a3a3a;
    --night-top: #3b3b3b;
    --night-mid: #1c1c1c;
    --night-deep: #0c0c0c;
    --light-text: #f2f2f2;
    --muted-text: #cfcfcf;
    --rule: #8a8a8a;
  }
  * { margin: 0; padding: 0; box-sizing: border-box; }
  html, body { width: 1200px; height: 950px; overflow: hidden; }
  body {
    background: var(--canvas);
    position: relative;
    font-family: "Arimo", Arial, sans-serif;
  }
  .card {
    position: absolute;
    left: 240px;
    width: 720px;
    height: 411px;
    overflow: hidden;
    box-shadow: 0 10px 30px rgba(0,0,0,.18);
  }
  .card--front { top: 44px; background: var(--paper); }
  .card--back { top: 495px; }
  .card-art { position: absolute; inset: 0; width: 100%; height: 100%; }

  /* Front: left identity */
  .identity {
    position: absolute;
    left: 28px;
    top: 78px;
    width: 330px;
    text-align: center;
    color: var(--ink);
    font-family: "Cinzel", "Times New Roman", serif;
    font-weight: 400;
  }
  .identity__mark {
    display: block;
    width: 46px;
    height: 46px;
    margin: 0 auto 14px;
    background: var(--ink);
  }
  .identity__prefix {
    display: block;
    font-size: 12px;
    letter-spacing: 4px;
    padding-bottom: 6px;
    border-bottom: 1px solid var(--rule);
    margin: 0 10px 6px;
  }
  .identity__name {
    display: block;
    font-size: 34px;
    line-height: 1.1;
    padding-bottom: 8px;
    border-bottom: 1px solid var(--rule);
    margin: 0 10px;
  }

  /* Front: right contact column */
  .contact {
    position: absolute;
    right: 30px;
    top: 120px;
    text-align: right;
    color: var(--light-text);
  }
  .contact__name {
    font-family: "Cinzel", "Times New Roman", serif;
    font-weight: 600;
    font-size: 26px;
    letter-spacing: 1px;
    line-height: 1.1;
  }
  .contact__role {
    font-family: "Cinzel", "Times New Roman", serif;
    font-size: 17px;
    color: var(--muted-text);
    letter-spacing: 1px;
    margin-bottom: 20px;
  }
  .contact__address, .contact__lines { font-size: 17px; line-height: 25px; font-style: normal; }
  .contact__address { margin-bottom: 4px; }
  .contact__line { display: flex; justify-content: flex-end; align-items: center; gap: 8px; }
  .contact__icon { width: 15px; height: 15px; fill: var(--light-text); flex: none; }

  /* Back */
  .back-identity {
    position: absolute;
    inset: 0;
    display: flex;
    flex-direction: column;
    align-items: center;
    justify-content: center;
    color: var(--light-text);
  }
  .back-identity__name {
    font-family: "Cinzel", "Times New Roman", serif;
    font-weight: 400;
    font-size: 52px;
    letter-spacing: 2px;
  }
  .back-identity__web {
    margin-top: 18px;
    font-size: 18px;
    letter-spacing: 3px;
    color: var(--muted-text);
  }
</style>
</head>
<body>

<section class="card card--front" aria-label="Business card front">
  <svg class="card-art" viewBox="0 0 720 411" preserveAspectRatio="none" aria-hidden="true">
    <defs>
      <linearGradient id="night" x1="0" y1="0" x2="1" y2="1">
        <stop offset="0" stop-color="var(--night-top)"/>
        <stop offset=".45" stop-color="var(--night-mid)"/>
        <stop offset="1" stop-color="var(--night-deep)"/>
      </linearGradient>
    </defs>
    <polygon points="440,0 720,0 720,411 275,411" fill="url(#night)"/>
    <polygon points="456,0 461,0 296,411 291,411" fill="var(--paper)"/>
  </svg>

  <div class="identity">
    <span class="identity__mark"></span>
    <span class="identity__prefix">Law Offices of</span>
    <span class="identity__name">Doran M. Vaske</span>
  </div>

  <div class="contact">
    <p class="contact__name">Doran M. Vaske</p>
    <p class="contact__role">CEO/Founder</p>
    <address class="contact__address">
      482 W. Harlow Ave.,<br>
      Suite 312<br>
      Pasadena, CA 91108
    </address>
    <div class="contact__lines">
      <p class="contact__line">626-503-7719
        <svg class="contact__icon" viewBox="0 0 16 16" aria-label="Telephone"><path d="M3 2h3l1 3-2 1.2a9 9 0 0 0 4.8 4.8L11 9l3 1v3a1 1 0 0 1-1 1A12 12 0 0 1 2 3a1 1 0 0 1 1-1z"/></svg>
      </p>
      <p class="contact__line">626-581-9046
        <svg class="contact__icon" viewBox="0 0 16 16" aria-label="Fax"><rect x="4" y="1" width="8" height="5"/><rect x="1" y="6" width="14" height="7" rx="1"/><rect x="4" y="10" width="8" height="5" fill="#1c1c1c"/><rect x="5" y="11" width="6" height="4"/></svg>
      </p>
      <p class="contact__line">dvaske@dmvlegalgrp.example
        <svg class="contact__icon" viewBox="0 0 16 16" aria-label="Email"><path d="M1 3h14v10H1z M1.8 3.6 8 8.6l6.2-5" stroke="#1c1c1c" stroke-width="1"/></svg>
      </p>
      <p class="contact__line">www.dmvlegalgrp.example
        <svg class="contact__icon" viewBox="0 0 16 16" aria-label="Website"><circle cx="8" cy="8" r="7"/><path d="M1 8h14M8 1c-3 3.5-3 10.5 0 14M8 1c3 3.5 3 10.5 0 14" stroke="#1c1c1c" stroke-width="1" fill="none"/></svg>
      </p>
    </div>
  </div>
</section>

<section class="card card--back" aria-label="Business card back">
  <svg class="card-art" viewBox="0 0 720 411" preserveAspectRatio="none" aria-hidden="true">
    <defs>
      <linearGradient id="nightBack" x1="0" y1="0" x2="1" y2="1">
        <stop offset="0" stop-color="var(--night-top)"/>
        <stop offset=".5" stop-color="var(--night-mid)"/>
        <stop offset="1" stop-color="var(--night-deep)"/>
      </linearGradient>
    </defs>
    <rect width="720" height="411" fill="url(#nightBack)"/>
  </svg>
  <div class="back-identity">
    <p class="back-identity__name">Doran M. Vaske</p>
    <p class="back-identity__web">www.dmvlegalgrp.example</p>
  </div>
</section>

</body>
</html>
```